Townhome Multi-Family Property Exterior Sign

Hello. We are looking for a new design for our exterior pylon for for a multi-family housing property in Texas. The design will need to go on a new sign panel to replace the existing (see photo of existing). We are looking to see both modern and contemporary designs. Included the sign should be the name, Loma Brisa Townhomes and the web address www.lomabrisatownhomes.example.

Attached here is a PDF file of the proposed new sign shape. We are open to other shape ideas as well if your design would better suit a more rectangular shape.

Industry/Entity Type

Property

Font styles to use
Serif
Sans Serif

Colors
9bcb3c

Requirements
Must have
• Name of building: Loma Brisa Townhomes
• Website: www.lomabrisatownhomes.example
Nice to have
• Address: 412-590 Halvern Ridge Drive (only if it fits nicely)

```html
<!DOCTYPE html>
<html lang="en">
<head>
<meta charset="utf-8">
<title>Loma Brisa Townhomes – Exterior Sign</title>
<link rel="stylesheet" href="https://fonts.googleapis.com/css2?family=Oswald:wght@700&family=Montserrat:wght@400;700&display=swap">
<style>
  :root {
    --leaf-green: #9bcb3c;
    --deep-green: #1d6a2b;
    --white: #ffffff;
    --page: #ffffff;
  }
  html, body {
    margin: 0;
    padding: 0;
    width: 1200px;
    height: 750px;
    overflow: hidden;
    background: var(--page);
  }
  .canvas {
    position: relative;
    width: 1200px;
    height: 750px;
  }
  .sign-shape {
    position: absolute;
    inset: 0;
  }
  .building-art {
    position: absolute;
    top: 292px;
    height: 236px;
    background: linear-gradient(180deg, rgba(29,106,43,0.25), rgba(29,106,43,0.45));
  }
  .building-art--left { left: 105px; width: 120px; }
  .building-art--right { left: 962px; width: 133px; }
  .brand-dot {
    position: absolute;
    left: 578px;
    top: 152px;
    width: 38px;
    height: 38px;
    border: 4px solid var(--white);
    border-radius: 50%;
  }
  .property-name {
    position: absolute;
    left: 0;
    width: 1200px;
    margin: 0;
    text-align: center;
    color: var(--white);
    font-family: "Oswald", "Arial Narrow", sans-serif;
    font-weight: 700;
    font-size: 122px;
    line-height: 1;
    text-transform: uppercase;
    letter-spacing: 1px;
  }
  .property-name--line1 { top: 236px; }
  .property-name--line2 { top: 334px; }
  .property-address {
    position: absolute;
    left: 0;
    top: 466px;
    width: 1200px;
    margin: 0;
    text-align: center;
    color: var(--white);
    font-family: "Montserrat", Arial, sans-serif;
    font-weight: 400;
    font-size: 32px;
    line-height: 1.2;
  }
  .property-web {
    position: absolute;
    left: 105px;
    top: 528px;
    width: 990px;
    height: 72px;
    margin: 0;
    display: flex;
    align-items: center;
    justify-content: center;
    color: var(--leaf-green);
    font-family: "Montserrat", Arial, sans-serif;
    font-weight: 700;
    font-size: 34px;
    letter-spacing: 0.5px;
  }
</style>
</head>
<body>
  <main class="canvas">
    <svg class="sign-shape" width="1200" height="750" viewBox="0 0 1200 750" aria-hidden="true">
      <path d="M105 247 C330 247 420 132 600 132 C780 132 870 247 1095 247 V528 H105 Z" fill="var(--leaf-green)"/>
      <rect x="105" y="528" width="990" height="72" fill="var(--deep-green)"/>
    </svg>

    <div class="building-art building-art--left" role="img" aria-label="Line illustration of two townhome facades"></div>
    <div class="building-art building-art--right" role="img" aria-label="Line illustration of two townhome facades"></div>

    <span class="brand-dot" aria-hidden="true"></span>

    <h1 class="property-name property-name--line1">Loma Brisa</h1>
    <p class="property-name property-name--line2">Townhomes</p>
    <p class="property-address">412-590 Halvern Ridge Drive</p>
    <p class="property-web">www.lomabrisatownhomes.example</p>
  </main>
</body>
</html>
```